Brisk Tails Dog Behaviour, Training and Natural Healthcare Website

Hey there,
I need a webpage designed for my new business. It needs to be something authentic, new, fresh and representative of my business ethos. I operate out of Newcastle, NSW. I believe my job is to keep dogs alive and in their home by promoting communication and connection between dogs and their owners. This can't be achieved through training and behaviour alone. Nutritional guidance and environmental adaptation are often needed to complete the package and increase the success rate for these programs. I provide practical services such as walking coaching, nutrition profiling, behavioural modification, puppy minding, board and train programs for puppies and young dogs, training, basic and complex skills training, physical therapies and natural healthcare options. In effect taking care of the whole dog.
My motto is = Happy dogs, happy owners.
My catch cry is = promoting communication and connection between dogs and their owners.

I have in mind pages that can also link to other pages when an icon is clicked. I need a homepage, sections to explain what each of my services do (4 - which could be independent pages so I can attach photos) and a gallery. I want to have multi page function, an online capability for future retail, ability to amend and update content myself, an online booking and payment facility. My interests lie in I have seen many successes via and environmental modifications.
I've attached the logo which features prominently on my business card and Chatterlane page. The corporate colours are Blue with a splash of red and white. The dog being held in the healing hands must feature.

Thanks!

Target Market(s)

Australian Pet Dog Owners

Colors
0355a3
ec1f27
ffffff

Requirements
Must have
• The business colours (blue with a splash of red and white), the dog in the healing hands
Should not have
• Pawprints or cartoon animals

```html
<!DOCTYPE html>
<html lang="en">
<head>
<meta charset="utf-8">
<title>Brisk Tails – Dog Behaviour, Training and Natural Healthcare</title>
<link rel="stylesheet" href="https://fonts.googleapis.com/css2?family=Open+Sans:wght@400;600;700&display=swap">
<style>
:root{
  --blue:#0355a3;
  --blue-dark:#024487;
  --red:#ec1f27;
  --white:#ffffff;
  --ink:#555;
  --muted:#8a8a8a;
  --rule:#d6d6d6;
  --band:#f2f2f2;
  --footer:#3b3b3b;
}
*{margin:0;padding:0;box-sizing:border-box}
html,body{width:734px;height:1200px;overflow:hidden;background:var(--white)}
body{position:relative;font-family:"Open Sans",Arial,sans-serif;color:var(--ink)}
h1,h2,h3{font-weight:400}
a{text-decoration:none}
.abs{position:absolute}

/* header */
.topline{left:0;top:0;width:734px;height:2px;background:var(--blue)}
.site-header{left:0;top:2px;width:734px;height:63px;background:var(--white);border-bottom:1px solid #e4e4e4}
.nav-link{position:absolute;top:27px;font-size:8px;color:#666;text-transform:uppercase;letter-spacing:.2px}
.nav-link.active{color:var(--blue)}
.brand{left:313px;top:23px;width:108px;height:58px;border-radius:50%;background:var(--blue);display:flex;align-items:center;justify-content:center;gap:5px}
.brand-dot{width:9px;height:9px;border-radius:50%;background:var(--white)}
.brand-name{font-size:10px;font-weight:700;color:var(--white);text-transform:uppercase}

/* hero */
.hero{left:0;top:66px;width:734px;height:324px;
  background:
    radial-gradient(ellipse 90px 120px at 300px 150px,rgba(40,80,140,.85),rgba(40,80,140,0) 100%),
    radial-gradient(ellipse 80px 90px at 540px 250px,rgba(90,60,45,.9),rgba(90,60,45,0) 100%),
    linear-gradient(180deg,rgba(0,0,0,0) 0%,rgba(0,0,0,0) 52%,rgba(0,0,0,0) 100%),
    linear-gradient(90deg,rgba(170,185,190,.75) 0%,rgba(170,185,190,.3) 35%,rgba(170,185,190,0) 60%),
    linear-gradient(180deg,#4d5e3a 0%,#6f7f55 25%,#9aa590 42%,#8fae4e 58%,#7f9f3c 80%,#6f8f33 100%)}
.hero-arrow{position:absolute;width:32px;height:32px}

/* welcome */
.welcome{left:60px;top:373px;width:614px;height:176px}
.welcome-title{left:105px;top:385px;font-size:14px;font-weight:700;line-height:19px;text-transform:uppercase}
.welcome-title .red{color:var(--red)}
.welcome-title .blue{color:var(--blue);display:block}
.dotted{left:105px;top:429px;width:228px;border-top:1px dotted #bbb}
.welcome-text{left:105px;top:437px;width:232px;font-size:6.6px;line-height:13.6px;color:var(--muted)}
.thumb-round{position:absolute;border-radius:50%;border:3px solid var(--white);box-shadow:0 0 0 1px #ddd}

/* services */
.section-title{font-size:14.5px;font-weight:600;color:#666;text-transform:uppercase}
.services-title{left:0;top:576px;width:734px;text-align:center}
.services-intro{left:140px;top:604px;width:454px;text-align:center;font-size:6.4px;line-height:13.6px;color:var(--muted)}
.service{position:absolute;top:648px;width:140px;text-align:center}
.service-photo{width:95px;height:95px;margin:0 auto;border-radius:50%;border:2px solid #e8e8e8;box-shadow:0 1px 3px rgba(0,0,0,.25)}
.service-name{margin-top:10px;font-size:9.6px;color:#333;text-transform:uppercase;letter-spacing:.2px}
.service-text{margin-top:5px;font-size:6.4px;line-height:11.4px;color:var(--muted)}
.btn{display:inline-block;margin-top:9px;width:65px;height:22px;line-height:22px;background:var(--blue);color:var(--white);font-size:7px;text-transform:uppercase;border:1px solid var(--blue-dark)}

/* info band */
.band{left:0;top:860px;width:734px;height:237px;background:var(--band)}
.col-title{position:absolute;top:873px;font-size:12.5px;color:#666;text-transform:uppercase}
.about-photo{left:61px;top:897px;width:185px;height:108px;
  background:
    radial-gradient(ellipse 22px 40px at 48px 55px,rgba(60,140,60,.9),rgba(60,140,60,0) 100%),
    radial-gradient(ellipse 22px 28px at 145px 70px,rgba(240,235,220,.95),rgba(240,235,220,0) 100%),
    linear-gradient(180deg,#c8dbe6 0%,#e6e4c8 45%,#a6bb62 68%,#8aa93f 85%,#6e8f33 100%);
  box-shadow:0 2px 3px rgba(0,0,0,.25)}
.about-caption{left:61px;top:1012px;font-size:7.5px;color:#444;text-transform:uppercase}
.about-text{left:61px;top:1027px;width:190px;font-size:6.4px;line-height:13.6px;color:var(--muted)}
.news{position:absolute;left:286px;width:170px}
.news-date{font-size:7.3px;color:#333;text-transform:uppercase}
.news-head{margin-top:4px;font-size:5.4px;line-height:11.8px;color:#444;text-transform:uppercase}
.news-text{margin-top:2px;font-size:6.2px;line-height:12px;color:var(--muted)}
.news-rule{left:286px;top:985px;width:160px;border-top:1px solid var(--rule)}
.post{position:absolute;left:490px;width:185px;height:60px}
.post-thumb{position:absolute;left:0;top:0;width:42px;height:39px;box-shadow:0 1px 2px rgba(0,0,0,.3)}
.post-title{position:absolute;left:54px;top:0;font-size:6.8px;color:#333;text-transform:uppercase}
.post-text{position:absolute;left:54px;top:12px;width:132px;font-size:6px;line-height:11.4px;color:var(--muted)}
.post-rule{position:absolute;left:490px;width:164px;border-top:1px solid var(--rule)}

/* footer */
.site-footer{left:0;top:1097px;width:734px;height:103px;background:var(--footer)}
.social-row{left:0;top:1116px;width:734px;display:flex;justify-content:center;gap:14px}
.social{display:flex;align-items:center;gap:4px;font-size:7px;color:#cfcfcf}
.social-dot{width:12px;height:12px;border-radius:50%;border:1px solid #9a9a9a}
.footer-nav{left:0;top:1150px;width:734px;text-align:center;font-size:6.4px;color:#999;text-transform:uppercase}
.footer-nav span{margin:0 8px}
.copyright{left:0;top:1174px;width:734px;text-align:center;font-size:6.4px;color:#888}
</style>
</head>
<body>

<div class="abs topline"></div>
<header class="abs site-header">
  <nav>
    <a class="nav-link active" style="left:80px">Home</a>
    <a class="nav-link" style="left:152px">About</a>
    <a class="nav-link" style="left:227px">Dog Breeds</a>
    <a class="nav-link" style="left:445px">Services</a>
    <a class="nav-link" style="left:528px">Training</a>
    <a class="nav-link" style="left:613px">Contacts</a>
  </nav>
</header>

<section class="abs hero" role="img" aria-label="Woman in a blue hoodie crouching on a lawn by a lake, holding a tennis ball while a brown puppy offers its paw"></section>
<svg class="abs hero-arrow" style="left:19px;top:211px" viewBox="0 0 32 32" aria-label="Previous slide"><circle cx="16" cy="16" r="14.5" fill="none" stroke="#fff" stroke-width="2"/><path d="M20 8 L10 16 L20 24 Z" fill="#fff"/></svg>
<svg class="abs hero-arrow" style="left:680px;top:211px" viewBox="0 0 32 32" aria-label="Next slide"><circle cx="16" cy="16" r="14.5" fill="none" stroke="#fff" stroke-width="2"/><path d="M12 8 L22 16 L12 24 Z" fill="#fff"/></svg>

<div class="abs brand"><span class="brand-dot"></span><span class="brand-name">Brisk Tails</span></div>

<svg class="abs welcome" viewBox="0 0 614 176" aria-hidden="true">
  <defs><filter id="cardShadow" x="-5%" y="-5%" width="110%" height="120%"><feDropShadow dx="0" dy="2" stdDeviation="3" flood-color="#000" flood-opacity=".18"/></filter></defs>
  <path d="M2 2 H612 V125 Q307 215 2 125 Z" fill="#fff" filter="url(#cardShadow)"/>
</svg>
<h1 class="abs welcome-title"><span class="red">Welcome to</span><span class="blue">Brisk Tails</span></h1>
<div class="abs dotted"></div>
<p class="abs welcome-text">Lorem ipsum dolor sit amet, consectetuer adipiscing elit. Aenean commodo ligula eget dolor. Aenean massa. Cum sociis natoque penatibus et magnis dis parturient montes, nascetur ridiculus mus. Donec quam felis, ultricies nec, fringilla vel, aliquet nec, vulputate eget, arcu.</p>
<div class="thumb-round" style="left:372px;top:405px;width:83px;height:83px;background:radial-gradient(circle at 38% 70%,#c79a52 0,#c79a52 18%,rgba(199,154,82,0) 40%),linear-gradient(180deg,#7fb0d6 0%,#5b8fb5 30%,#d6c3a0 60%,#b59263 100%)" role="img" aria-label="Woman sitting on a beach with a golden retriever"></div>
<div class="thumb-round" style="left:467px;top:405px;width:83px;height:83px;background:radial-gradient(circle at 30% 55%,#3f8a3e 0,rgba(63,138,62,0) 22%),radial-gradient(circle at 65% 60%,#f1ede2 0,rgba(241,237,226,0) 20%),linear-gradient(180deg,#d8e6f0 0%,#c6d6a0 50%,#98b84a 75%,#7a9e32 100%)" role="img" aria-label="Woman playing with a white dog in a park"></div>
<div class="thumb-round" style="left:564px;top:405px;width:83px;height:83px;background:radial-gradient(circle at 40% 30%,#9bb3a0 0,rgba(155,179,160,0) 35%),radial-gradient(circle at 45% 75%,#1f2226 0,rgba(31,34,38,0) 35%),linear-gradient(180deg,#8ea3ad 0%,#5a6870 50%,#363d43 100%)" role="img" aria-label="Woman driving a car with a dog on the passenger side"></div>

<h2 class="abs section-title services-title">Our Services</h2>
<p class="abs services-intro">Lorem ipsum dolor sit amet, consec tetuer adipiscing. Praesent vestibu lum molestie lacuiirhs. Aenean non ummy hendreriauris. Phasellus. porta. Fusce suscipit varius mium sociis totdnatibus et magis dis parturient montes, nascetur ridiculus mus.</p>

<article class="service" style="left:65px">
  <div class="service-photo" role="img" aria-label="Person walking several dogs on leads along a park path" style="background:radial-gradient(circle at 30% 55%,#4a6a9a 0,rgba(74,106,154,0) 25%),radial-gradient(circle at 70% 70%,#e8e6e0 0,rgba(232,230,224,0) 25%),linear-gradient(180deg,#5f9a3a 0%,#8fbd5e 40%,#c3cbb8 75%,#d4d4cc 100%)"></div>
  <h3 class="service-name">Walking Coaching</h3>
  <p class="service-text">Sed ut perspiciatis unde omnis iste natus error sit voluptatem accusantium doloremque laudantium explicabo.</p>
  <a class="btn">Read More</a>
</article>
<article class="service" style="left:218px">
  <div class="service-photo" role="img" aria-label="Woman lying on a bed cuddling a small white dog" style="background:radial-gradient(circle at 40% 40%,#e8b878 0,rgba(232,184,120,0) 28%),radial-gradient(circle at 45% 75%,#f7f5f0 0,rgba(247,245,240,0) 30%),linear-gradient(180deg,#bcd8e6 0%,#e6d9c8 50%,#dcb48c 100%)"></div>
  <h3 class="service-name">Puppy Minding</h3>
  <p class="service-text">Sed ut perspiciatis unde omnis iste natus error sit voluptatem accusantium doloremque laudantium explicabo.</p>
  <a class="btn">Read More</a>
</article>
<article class="service" style="left:375px">
  <div class="service-photo" role="img" aria-label="Cream labrador puppy lying on green grass" style="background:radial-gradient(ellipse 40% 35% at 52% 55%,#f2ead8 0,#e8dcc2 60%,rgba(232,220,194,0) 100%),linear-gradient(180deg,#5f8e32 0%,#7faa45 45%,#5f8f2a 100%)"></div>
  <h3 class="service-name">Young Dogs</h3>
  <p class="service-text">Sed ut perspiciatis unde omnis iste natus error sit voluptatem accusantium doloremque laudantium explicabo.</p>
  <a class="btn">Read More</a>
</article>
<article class="service" style="left:527px">
  <div class="service-photo" role="img" aria-label="Woman on a beach throwing a ball for a leaping dog" style="background:radial-gradient(ellipse 12% 30% at 55% 60%,#3e5a80 0,rgba(62,90,128,0) 100%),linear-gradient(180deg,#c6d8e8 0%,#a9bfd2 45%,#8fa4b6 58%,#d9ccb2 72%,#cbb894 100%)"></div>
  <h3 class="service-name">Walking Coaching</h3>
  <p class="service-text">Sed ut perspiciatis unde omnis iste natus error sit voluptatem accusantium doloremque laudantium explicabo.</p>
  <a class="btn">Read More</a>
</article>

<div class="abs band"></div>

<h2 class="col-title" style="left:61px">About Us</h2>
<div class="abs about-photo" role="img" aria-label="Woman in a green shirt training a white dog that stands on its hind legs in a park"></div>
<h3 class="abs about-caption">Lorem ipsum dolor sit amet consec</h3>
<p class="abs about-text">Sed ut perspiciatis unde omnis iste natus error sit voluptatem accusantium doloremque laudantium, totam rem aperiam, eaque ipsa quae ab illo inventore veritatis et quasi architecto beatae vitae dicta sunt explicabo.</p>

<h2 class="col-title" style="left:282px">Recent News</h2>
<article class="news" style="top:900px">
  <div class="news-date">Dec 25, 2014</div>
  <div class="news-head">Lorem ipsum dolor sit amet, consec teer adipiscing.<br>Prsent vestibulum.</div>
  <p class="news-text">Lorem ipsum dolor sit amet, consec tetuer adipi scing. Praesent vestibu lum molestie lacuiirhs. Aenean non ummy hendreriauris Phasellus.</p>
</article>
<div class="abs news-rule"></div>
<article class="news" style="top:1001px">
  <div class="news-date">Dec 25, 2014</div>
  <div class="news-head">Lorem ipsum dolor sit amet, consec teer adipiscing.<br>Prsent vestibulum.</div>
  <p class="news-text">Lorem ipsum dolor sit amet, consec tetuer adipi scing. Praesent vestibu lum molestie lacuiirhs. Aenean non ummy hendreriauris Phasellus.</p>
</article>

<h2 class="col-title" style="left:490px">Latest Blog</h2>
<article class="post" style="top:901px">
  <div class="post-thumb" role="img" aria-label="Woman kneeling beside a dog on a path" style="background:radial-gradient(circle at 35% 55%,#2f4f7a 0,rgba(47,79,122,0) 35%),linear-gradient(180deg,#7f98ae 0%,#56687a 55%,#3d4650 100%)"></div>
  <h3 class="post-title">Neque porro quisquam</h3>
  <p class="post-text">Sed ut perspiciatis unde omnis iste sit volup-tatem accusantium aperiam Sed ut laudan-tium, totam rem aperiam</p>
</article>
<div class="post-rule" style="top:962px"></div>
<article class="post" style="top:972px">
  <div class="post-thumb" role="img" aria-label="Woman with a white dog by the water" style="background:radial-gradient(circle at 60% 65%,#e6eef0 0,rgba(230,238,240,0) 30%),linear-gradient(180deg,#4f9aa6 0%,#3c7f7a 55%,#3a5e48 100%)"></div>
  <h3 class="post-title">Neque porro quisquam</h3>
  <p class="post-text">Sed ut perspiciatis unde omnis iste sit volup-tatem accusantium aperiam Sed ut laudan-tium, totam rem aperiam</p>
</article>
<div class="post-rule" style="top:1030px"></div>
<article class="post" style="top:1042px">
  <div class="post-thumb" role="img" aria-label="Girl sitting with a dog on a wooden deck" style="background:radial-gradient(circle at 35% 55%,#c8a8d8 0,rgba(200,168,216,0) 30%),radial-gradient(circle at 70% 65%,#b0784a 0,rgba(176,120,74,0) 28%),linear-gradient(180deg,#9aa7b4 0%,#8e8c86 50%,#8a6a4c 100%)"></div>
  <h3 class="post-title">Neque porro quisquam</h3>
  <p class="post-text">Sed ut perspiciatis unde omnis iste sit volup-tatem accusantium aperiam Sed ut laudan-tium, totam rem aperiam</p>
</article>

<footer class="abs site-footer"></footer>
<nav class="abs social-row" aria-label="Social links">
  <a class="social"><span class="social-dot"></span>Chatterlane</a>
  <a class="social"><span class="social-dot"></span>Chirpwire</a>
  <a class="social"><span class="social-dot"></span>Globenote</a>
  <a class="social"><span class="social-dot"></span>ClipHarbor</a>
  <a class="social"><span class="social-dot"></span>Feedline</a>
</nav>
<nav class="abs footer-nav"><span>Home</span>/<span>About</span>/<span>Dog Breeds</span>/<span>Training</span>/<span>Contacts</span></nav>
<p class="abs copyright">© copy Rights 2014 Brisk Tails All Rights Reserved.</p>

</body>
</html>
```